Seven Slides with Charts for Sales Presentation

We have the basic concept for seven important slides we need, but want to have them graphically pleasing beyond what we could do with standard charts and powerpoint. We are a software company. Attaching whiteboard versions of the slides and one graphic (slide 7). The graphics can be combined into animated slides, I will be happy to explain.

Target Market(s)

Decision Makers / Board Members for Professional Associations. For example, we are presenting to a State Association of Pharmacists next week.

Industry/Entity Type

Sales

Font styles to use
Sans Serif

Colors
33a6d7
00a990

Requirements
Must have
• Quality Graphics. I have more detail for the first slide too. You can look at http://dev.plumvessel.example for a sneak peek.
Nice to have
• Web "3.0" look and feel. Tablet / mobile friendly look.
Should not have
• Clip art or anything unprofessional.

```html
<!DOCTYPE html>
<html lang="en">
<head>
<meta charset="utf-8">
<title>Quintara – Sales Presentation Slides</title>
<link href="https://fonts.googleapis.com/css2?family=Open+Sans:wght@400;600;700&family=Oswald:wght@500;600&display=swap" rel="stylesheet">
<style>
  :root{
    --board:#a6a6a6;
    --paper:#ffffff;
    --green:#0e9647;
    --green-mid:#0b7d3c;
    --green-deep:#0a6a35;
    --green-dark:#053c1e;
    --charcoal:#3d3d3f;
    --grey:#bcbcbc;
    --grey-mid:#9d9d9d;
    --rule:#dcdcdc;
    --ink:#333333;
    --muted:#666666;
  }
  *{margin:0;padding:0;box-sizing:border-box}
  html,body{width:1200px;height:926px;overflow:hidden;background:var(--board)}
  body{font-family:"Open Sans",Arial,sans-serif;color:var(--ink)}
  .board{position:absolute;left:0;top:0;width:1166px;height:900px;transform:scale(1.0292);transform-origin:0 0}
  .slide{position:absolute;width:362px;height:272px;background:var(--paper);overflow:hidden}
  .abs{position:absolute}

  /* shared slide header */
  .slide-title{position:absolute;left:32px;top:14px;font-size:12.5px;font-weight:700;color:var(--green);letter-spacing:.3px}
  .title-rule{position:absolute;left:32px;top:35px;width:143px;height:2px;background:var(--green)}
  .title-rule-rest{position:absolute;left:175px;top:36px;right:0;height:1px;background:var(--rule)}
  .brand{position:absolute;right:14px;top:14px;display:flex;align-items:center;gap:4px;font-size:12px;font-weight:700;color:var(--ink);letter-spacing:-.2px}
  .brand-mark{width:10px;height:10px;background:var(--charcoal)}
  .page-no{position:absolute;right:0;bottom:0;width:13px;height:13px;background:#222;color:#fff;font-size:6.5px;font-weight:700;display:flex;align-items:center;justify-content:center}

  /* slide 1 – cover */
  .cover-photo{position:absolute;left:0;top:0;width:362px;height:208px;background:linear-gradient(180deg,#a9b9c6 0%,#c4ccd1 55%,#9c9a8c 85%,#6f6a5d 100%)}
  .cover-title{position:absolute;left:30px;top:92px;width:178px;height:24px;background:var(--green);color:#fff;font-size:14.5px;font-weight:600;padding-left:6px;line-height:24px;letter-spacing:.3px}
  .cover-intro{position:absolute;left:30px;top:120px;width:221px;height:44px;background:var(--green);color:#fff;font-size:5px;line-height:6.4px;padding:4px 5px}
  .cover-brand{position:absolute;left:35px;top:229px;display:flex;align-items:center;gap:6px;font-size:18px;font-weight:600;color:var(--ink);letter-spacing:.2px}
  .cover-brand .brand-mark{width:14px;height:14px}
  .cover-web{position:absolute;left:260px;top:243px;font-size:7.5px;color:var(--ink)}

  /* slide 2 – association grid */
  .assoc-name{position:absolute;left:42px;top:18px;display:flex;align-items:center;gap:10px;font-size:8.5px;color:var(--ink)}
  .assoc-name .brand-mark{width:9px;height:9px}
  .tag{position:absolute;left:39px;top:50px;height:15px;padding:0 4px;background:var(--green);color:#fff;font-size:7px;line-height:15px}
  .tag-line{position:absolute;left:41px;top:69px;font-size:7px;color:var(--ink)}
  .tile{position:absolute;width:76px}
  .tile-box{width:76px;height:61px;background:var(--green)}
  .tile-name{font-size:6.5px;font-weight:600;margin-top:5px;line-height:7px}
  .tile-sub{font-size:4.5px;color:var(--muted);line-height:5px}

  /* slide 3 – revenue */
  .alloc-pct{position:absolute;left:166px;font-size:17px;font-weight:700;color:var(--green)}
  .alloc-label{position:absolute;left:234px;font-size:8px;line-height:10px;color:var(--muted)}
  .alloc-big{position:absolute;left:233px;top:196px;font-size:17.5px;font-weight:700;color:var(--green);letter-spacing:.5px}
  .seg{position:absolute;left:38px;width:111px;display:flex;align-items:center;justify-content:center}

  /* slide 4 – proceeds */
  .proc-pct{position:absolute;font-size:19px;font-weight:700;color:var(--green)}
  .proc-box{position:absolute;left:121px;top:91px;width:111px;height:110px;color:#fff;text-align:center;font-size:8.5px;line-height:11px}
  .proc-top{height:34px;background:var(--green-deep);display:flex;align-items:center;justify-content:center}
  .proc-bottom{height:76px;background:var(--green-dark);display:flex;align-items:center;justify-content:center;padding:0 10px}

  /* payout labels */
  .payout{position:absolute;display:flex;align-items:center;gap:4px;font-family:"Oswald",Arial,sans-serif;font-weight:500;font-size:19px;line-height:24px}
  .pct-box{width:46px;height:25px;color:#fff;text-align:center}
  .is-green .pct-box{background:var(--green)} .is-green .payout-name{color:var(--green)}
  .is-dark .pct-box{background:var(--charcoal)} .is-dark .payout-name{color:var(--charcoal)}
  .is-grey .pct-box{background:var(--grey)} .is-grey .payout-name{color:var(--grey)}
  .rating{position:absolute;font-size:7px;letter-spacing:-.5px;color:var(--charcoal)}
  .traits{position:absolute;font-size:7px;line-height:8.5px;color:var(--charcoal);list-style:none}

  /* slide 7 – phases */
  .chart-note{position:absolute;font-size:6.5px;line-height:7.5px;color:var(--muted);text-align:center}
  .phase-tag{position:absolute;font-size:6.5px;line-height:8px;font-weight:700;color:#fff;text-align:right}
  .axis-label{position:absolute;font-size:7px;color:var(--muted)}

  /* slide 8 – approval matrix */
  .col-head{position:absolute;top:95px;font-size:4.5px;line-height:5.5px;font-weight:700;text-align:center;color:var(--ink)}
  .row-head{position:absolute;left:44px;font-size:4.5px;font-weight:700;color:var(--ink)}
  .cell{position:absolute;background:var(--charcoal)}
  .cell.on{background:var(--green)}

  /* slide 9 – closing */
  .closing-photo{position:absolute;inset:0;background:linear-gradient(180deg,#6f8fb5 0%,#a7a9b6 30%,#d8b79a 48%,#5d6678 62%,#2f3647 100%)}
  .closing-band{position:absolute;left:0;right:0;top:200px;bottom:0;background:#3e3e40}
  .thanks{position:absolute;left:54px;top:79px;width:261px;height:57px;background:var(--green);color:#fff;font-size:39px;line-height:57px;text-align:center;font-weight:400;letter-spacing:.5px}
  .contact-icon{position:absolute;top:190px;width:20px;height:20px;background:var(--green);display:flex;align-items:center;justify-content:center}
  .contact-text{position:absolute;top:224px;font-size:7px;line-height:9px;color:#fff;text-align:center}
</style>
</head>
<body>
<div class="board">

  <!-- 1 cover -->
  <section class="slide" style="left:23px;top:23px">
    <div class="cover-photo" role="img" aria-label="Photograph of a Paris skyline with a tall iron tower under a pale sky"></div>
    <div class="cover-title">PRESENTATION TITTLE</div>
    <p class="cover-intro">Lorem ipsum dolor sit amet, consectetur adipisicing elit, sed do eiusmod tempor incididunt ut labore et dolore magna aliqua. Ut enim ad minim veniam, quis nostrud. Lorem ipsum dolor sit amet, consectetur adipisicing elit, sed do eiusmod tempor incididunt ut labore et dolore magna aliqua. Ut enim ad minim veniam, quis nostrud</p>
    <div class="cover-brand"><span class="brand-mark"></span>QUINTARA</div>
    <div class="cover-web">www.website.com</div>
  </section>

  <!-- 2 association -->
  <section class="slide" style="left:402px;top:23px">
    <div class="assoc-name"><span class="brand-mark"></span>TN Association of Rocket Scientist</div>
    <div class="tag">lorem Ipsum Dolor sit</div>
    <div class="tag-line">lorem Ipsum Dolor sit amet amet jabang bayi</div>
    <div class="tile" style="left:40px;top:92px"><div class="tile-box"></div><div class="tile-name">lorem Ipsum</div><div class="tile-sub">Rating</div></div>
    <div class="tile" style="left:132px;top:92px"><div class="tile-box"></div><div class="tile-name">lorem Ipsum</div><div class="tile-sub">Rating</div></div>
    <div class="tile" style="left:223px;top:92px"><div class="tile-box"></div><div class="tile-name">lorem Ipsum</div><div class="tile-sub">Rating</div></div>
    <div class="tile" style="left:40px;top:177px"><div class="tile-box"></div><div class="tile-name">lorem Ipsum</div><div class="tile-sub">Rating</div></div>
    <div class="tile" style="left:132px;top:177px"><div class="tile-box"></div><div class="tile-name">lorem Ipsum</div><div class="tile-sub">Rating</div></div>
    <div class="tile" style="left:223px;top:177px"><div class="tile-box"></div><div class="tile-name">lorem Ipsum</div><div class="tile-sub">Rating</div></div>
  </section>

  <!-- 3 revenue allocation -->
  <section class="slide" style="left:782px;top:23px">
    <div class="slide-title">REVENUE ALLOCATION</div>
    <div class="title-rule"></div><div class="title-rule-rest"></div>
    <div class="brand"><span class="brand-mark"></span>QUINTARA</div>
    <div class="seg" style="top:61px;height:51px;background:var(--green)">
      <svg width="10" height="10" viewBox="0 0 10 10"><rect x="1" y="1" width="8" height="8" rx="1" fill="#fff"/><rect x="4.5" y="1" width="1" height="8" fill="var(--green)"/></svg>
    </div>
    <div class="seg" style="top:112px;height:24px;background:var(--green-mid)">
      <svg width="9" height="8" viewBox="0 0 9 8"><path d="M1 3h2l4-2v6L3 5H1z" fill="#fff"/></svg>
    </div>
    <div class="seg" style="top:136px;height:16px;background:var(--green-deep)">
      <svg width="8" height="7" viewBox="0 0 8 7"><rect x="1" y="1" width="6" height="5" fill="#fff"/><rect x="1" y="2.5" width="6" height="1" fill="var(--green-deep)"/></svg>
    </div>
    <div class="seg" style="top:152px;height:97px;background:var(--green-dark)">
      <svg width="11" height="11" viewBox="0 0 11 11"><circle cx="5.5" cy="5.5" r="3.6" fill="none" stroke="#fff" stroke-width="1.6" stroke-dasharray="1.6 1"/><circle cx="5.5" cy="5.5" r="1.2" fill="#fff"/></svg>
    </div>
    <div class="alloc-pct" style="top:72px">25%</div>
    <div class="alloc-label" style="top:74px">Software license<br>accounting adminis-<br>tration</div>
    <div class="alloc-pct" style="top:114px">10%</div>
    <div class="alloc-label" style="top:117px">Advertising</div>
    <div class="alloc-pct" style="top:136px">3-5%</div>
    <div class="alloc-label" style="top:138px">Credit card transac-<br>tion fees association<br>specific expenses</div>
    <div class="alloc-pct" style="top:197px">60%</div>
    <div class="alloc-big">PROCEEDS</div>
    <div class="page-no">3</div>
  </section>

  <!-- 4 proceeds -->
  <section class="slide" style="left:23px;top:317px">
    <div class="slide-title">PROCEEDS</div>
    <div class="title-rule"></div><div class="title-rule-rest"></div>
    <div class="brand"><span class="brand-mark"></span>QUINTARA</div>
    <div class="proc-pct" style="left:55px;top:96px">25%</div>
    <div class="proc-box">
      <div class="proc-top">Paid to Association</div>
      <div class="proc-bottom">TN Contribution<br>to<br>Instructor Payout<br>Pool</div>
    </div>
    <div class="proc-pct" style="left:250px;top:157px">75%</div>
    <div class="page-no">4</div>
  </section>

  <!-- 5 payout pool pie -->
  <section class="slide" style="left:402px;top:317px">
    <div class="slide-title">INSTRUCTOR PAYOUT POOL</div>
    <div class="title-rule"></div><div class="title-rule-rest"></div>
    <div class="brand"><span class="brand-mark"></span>QUINTARA</div>
    <svg class="abs" style="left:0;top:0" width="362" height="272" viewBox="0 0 362 272" role="img" aria-label="Pie chart of instructor payout shares">
      <path d="M96 153 L96 89 A64 64 0 0 1 160 153 Z" fill="var(--charcoal)"/>
      <path d="M96 153 L160 153 A64 64 0 0 1 123.1 211 Z" fill="var(--grey)"/>
      <path d="M96 153 L123.1 211 A64 64 0 1 1 96 89 Z" fill="var(--green)"/>
      <g stroke="#8a8a8a" stroke-width=".8" fill="none">
        <polyline points="86,170 86,86 208,86"/>
        <polyline points="136,141 208,141 208,132"/>
        <polyline points="128,184 160,184 160,178 208,178"/>
      </g>
      <g fill="#8a8a8a"><circle cx="86" cy="170" r="1.6"/><circle cx="208" cy="86" r="1.6"/><circle cx="136" cy="141" r="1.6"/><circle cx="208" cy="132" r="1.6"/><circle cx="128" cy="184" r="1.6"/><circle cx="208" cy="178" r="1.6"/></g>
    </svg>
    <div class="payout is-green" style="left:223px;top:75px"><span class="pct-box">35%</span><span class="payout-name">SALLY</span></div>
    <div class="payout is-dark" style="left:223px;top:120px"><span class="pct-box">35%</span><span class="payout-name">JOHNY</span></div>
    <div class="payout is-grey" style="left:223px;top:166px"><span class="pct-box">35%</span><span class="payout-name">GEORGE</span></div>
    <div class="page-no">5</div>
  </section>

  <!-- 6 payout pool ratings -->
  <section class="slide" style="left:782px;top:317px">
    <div class="slide-title">INSTRUCTOR PAYOUT POOL</div>
    <div class="title-rule"></div><div class="title-rule-rest"></div>
    <div class="brand"><span class="brand-mark"></span>QUINTARA</div>
    <svg class="abs" style="left:0;top:0" width="362" height="272" viewBox="0 0 362 272" role="img" aria-label="Pie chart of instructor payout shares by rating">
      <path d="M98 153 L98 89 A64 64 0 0 1 161.8 158.6 Z" fill="var(--charcoal)"/>
      <path d="M98 153 L161.8 158.6 A64 64 0 0 1 156 180 Z" fill="var(--grey)"/>
      <path d="M98 153 L156 180 A64 64 0 1 1 98 89 Z" fill="var(--green)"/>
      <g stroke="#8a8a8a" stroke-width=".8" fill="none">
        <polyline points="128,96 128,91 210,91"/>
        <polyline points="126,155 126,148 160,148 160,147 210,147"/>
        <polyline points="126,192 126,198 210,198"/>
      </g>
      <g fill="#8a8a8a"><circle cx="128" cy="96" r="1.6"/><circle cx="126" cy="155" r="1.6"/><circle cx="126" cy="192" r="1.6"/></g>
    </svg>
    <div class="payout is-dark" style="left:215px;top:73px"><span class="pct-box">25%</span><span class="payout-name">SALLY</span></div>
    <div class="rating" style="left:216px;top:98px">★★★★★</div>
    <ul class="traits" style="left:266px;top:100px"><li>• Engaging</li><li>• Timely</li><li>• Hgihly relevent</li></ul>
    <div class="payout is-grey" style="left:215px;top:139px"><span class="pct-box">25%</span><span class="payout-name">GEORGE</span></div>
    <div class="rating" style="left:216px;top:164px">★★★</div>
    <ul class="traits" style="left:266px;top:166px"><li>• Entertaining</li><li>• Dated</li></ul>
    <div class="payout is-green" style="left:215px;top:195px"><span class="pct-box">25%</span><span class="payout-name">JOHNY</span></div>
    <div class="rating" style="left:216px;top:220px">★★</div>
    <div class="page-no">6</div>
  </section>

  <!-- 7 growth phases -->
  <section class="slide" style="left:23px;top:608px">
    <div class="slide-title">INSTRUCTOR PAYOUT POOL</div>
    <div class="title-rule"></div><div class="title-rule-rest"></div>
    <div class="brand"><span class="brand-mark"></span>QUINTARA</div>
    <svg class="abs" style="left:0;top:0" width="362" height="272" viewBox="0 0 362 272" role="img" aria-label="Area chart of lesson quantity over time across three phases">
      <polygon points="65,205 152,160 152,205" fill="var(--green)"/>
      <polygon points="152,205 152,160 240,115 240,205" fill="var(--charcoal)"/>
      <polygon points="240,205 240,115 328,70 328,205" fill="var(--grey-mid)"/>
      <line x1="152" y1="130" x2="152" y2="205" stroke="var(--green)" stroke-width="1"/>
      <circle cx="152" cy="130" r="2" fill="var(--green)"/>
      <line x1="240" y1="90" x2="240" y2="205" stroke="var(--green)" stroke-width="1"/>
      <circle cx="240" cy="90" r="2" fill="var(--green)"/>
      <line x1="47" y1="82" x2="47" y2="238" stroke="#999" stroke-width=".8"/>
      <line x1="47" y1="238" x2="326" y2="238" stroke="#999" stroke-width=".8"/>
    </svg>
    <div class="chart-note" style="left:96px;top:121px">COMPETION<br>ENSUES</div>
    <div class="chart-note" style="left:200px;top:82px">QUALITY<br>SATURATION</div>
    <div class="phase-tag" style="left:120px;top:183px">PHASE<br>ONE</div>
    <div class="phase-tag" style="left:207px;top:183px">PHASE<br>TWO</div>
    <div class="phase-tag" style="left:294px;top:183px">PHASE<br>THREE</div>
    <div class="chart-note" style="left:70px;top:208px">Higher Convenious<br>Current Standart</div>
    <div class="chart-note" style="left:153px;top:208px">Competion drives<br>Quality Improvement</div>
    <div class="chart-note" style="left:261px;top:208px">Diversification +<br>Specialization</div>
    <div class="axis-label" style="left:185px;top:245px">TIME</div>
    <div class="axis-label" style="left:-8px;top:150px;transform:rotate(-90deg);transform-origin:center;width:90px;text-align:center">QUANTITY OF LESSON</div>
    <div class="page-no">7</div>
  </section>

  <!-- 8 approval matrix -->
  <section class="slide" style="left:402px;top:608px">
    <div class="slide-title">INSTRUCTOR PAYOUT POOL</div>
    <div class="title-rule"></div><div class="title-rule-rest"></div>
    <div class="brand"><span class="brand-mark"></span>QUINTARA</div>
    <div class="col-head" style="left:85px;width:46px">APPROVE<br>EVERYTHING</div>
    <div class="col-head" style="left:136px;width:62px">AUTO-APPROVE<br>BY REQUIREMENTS</div>
    <div class="col-head" style="left:203px;width:63px">SUGGEST APPROVAL<br>BY REQUIREMENTS</div>
    <div class="col-head" style="left:271px;width:46px">APPROVE<br>MANUALLY</div>
    <div class="row-head" style="top:126px">PUBLISHER</div>
    <div class="row-head" style="top:155px">INSTRUCTOR</div>
    <div class="row-head" style="top:186px">LESSON</div>

    <div class="cell on" style="left:85px;top:116px;width:46px;height:25px"></div>
    <div class="cell" style="left:136px;top:116px;width:62px;height:25px"></div>
    <div class="cell" style="left:203px;top:116px;width:63px;height:25px"></div>
    <div class="cell" style="left:271px;top:116px;width:46px;height:25px"></div>

    <div class="cell" style="left:85px;top:146px;width:46px;height:25px"></div>
    <div class="cell on" style="left:136px;top:146px;width:62px;height:25px"></div>
    <div class="cell" style="left:203px;top:146px;width:63px;height:25px"></div>
    <div class="cell" style="left:271px;top:146px;width:46px;height:25px"></div>

    <div class="cell" style="left:85px;top:176px;width:46px;height:25px"></div>
    <div class="cell" style="left:136px;top:176px;width:62px;height:25px"></div>
    <div class="cell on" style="left:203px;top:176px;width:63px;height:25px"></div>
    <div class="cell" style="left:271px;top:176px;width:46px;height:25px"></div>
    <div class="page-no">6</div>
  </section>

  <!-- 9 closing -->
  <section class="slide" style="left:782px;top:608px">
    <div class="closing-photo" role="img" aria-label="Photograph of a city skyline at dusk with skyscrapers under a warm sky"></div>
    <div class="closing-band"></div>
    <div class="thanks">THANK YOU</div>
    <div class="contact-icon" style="left:61px">
      <svg width="10" height="12" viewBox="0 0 10 12"><path d="M5 0.5a4 4 0 0 1 4 4c0 3-4 7-4 7s-4-4-4-7a4 4 0 0 1 4-4z" fill="#fff"/><circle cx="5" cy="4.5" r="1.5" fill="var(--green)"/></svg>
    </div>
    <div class="contact-icon" style="left:144px">
      <svg width="11" height="11" viewBox="0 0 11 11"><path d="M2 1l2 0 1 3-1.3 1a6 6 0 0 0 2.3 2.3L7 6l3 1v2a1 1 0 0 1-1 1A8 8 0 0 1 1 2a1 1 0 0 1 1-1z" fill="#fff"/></svg>
    </div>
    <div class="contact-icon" style="left:218px">
      <svg width="11" height="8" viewBox="0 0 11 8"><rect x="0.5" y="0.5" width="10" height="7" fill="#fff"/><path d="M0.5 0.5l5 4 5-4" fill="none" stroke="var(--green)" stroke-width="1"/></svg>
    </div>
    <div class="contact-icon" style="left:294px">
      <svg width="11" height="8" viewBox="0 0 11 8"><rect x="0.5" y="0.5" width="10" height="7" fill="#fff"/><path d="M0.5 0.5l5 4 5-4" fill="none" stroke="var(--green)" stroke-width="1"/></svg>
    </div>
    <div class="contact-text" style="left:22px;width:100px">48 Harbor Lane,Suite 210<br>Millbrook, NY 10020</div>
    <div class="contact-text" style="left:124px;width:60px">800.555.0142</div>
    <div class="contact-text" style="left:190px;width:76px">email@website.com</div>
    <div class="contact-text" style="left:268px;width:72px">www.website.com</div>
  </section>

</div>
</body>
</html>
```